E-Blast with US football theme

Hello, we are looking for an email blast with a US football theme (Crown Clash in the US is next weekend).
Specs:
600px w x 1500px h
Headline: Need Financing For A Win?
Winning teams donβt leave success to chanceβthey build a solid game plan.
Whether youβre expanding, constructing, refinancing, or making key acquisitions, RVM provides financing solutions that help you execute your strategy with confidence. Letβs work together to create a winning playbook.
Our custom financing solutions include:
π Acquisitions
π Construction
π Refinancing
π Recapitalizations
π Structured Leases
And our products include:
π Bridge
π Mezzanine
π Unitranche
π NNN Lease
π Preferred Equity

```html
<!DOCTYPE html>
<html lang="en">
<head>
<meta charset="utf-8">
<title>RVM – Need Financing For A Win?</title>
<link href="https://fonts.googleapis.com/css2?family=Bebas+Neue&family=Poppins:wght@400;700;800&display=swap" rel="stylesheet">
<style>
  :root {
    --night: #040816;
    --navy: #0c1d4f;
    --ink: #17254f;
    --royal: #0b3a94;
    --sky: #5fb4ee;
    --ice: #c9e6fb;
    --accent: #3d93ea;
    --white: #ffffff;
    --leather: #7a3e1e;
    --gold: #f0b323;
  }
  * { box-sizing: border-box; margin: 0; padding: 0; }
  html, body { width: 1200px; height: 3000px; overflow: hidden; background: var(--white); }
  body { font-family: "Poppins", sans-serif; position: relative; }

  .hero {
    position: absolute; left: 0; top: 0; width: 1200px; height: 2000px;
    background: var(--night); overflow: hidden;
  }
  .hero-photo {
    position: absolute; left: 0; top: 700px; width: 1200px; height: 1300px;
    background:
      radial-gradient(ellipse 420px 520px at 820px 520px, #1f5a4c 0%, rgba(31,90,76,0) 70%),
      radial-gradient(ellipse 420px 300px at 760px 1050px, #b8271c 0%, rgba(184,39,28,0) 70%),
      linear-gradient(180deg, #040816 0%, #0d1a2e 45%, #2a2a35 80%, #1a1d28 100%);
  }
  .hero-stripes { position: absolute; right: 0; top: 0; }
  .hero-chevrons { position: absolute; left: 0; top: 1450px; }

  .brand {
    position: absolute; left: 80px; top: 96px;
    display: flex; align-items: center; gap: 24px;
    font-weight: 800; font-size: 92px; color: var(--white); letter-spacing: 2px;
  }
  .brand-square { width: 60px; height: 60px; background: var(--white); }

  .headline {
    position: absolute; left: 70px; top: 352px;
    font-family: "Bebas Neue", sans-serif; font-size: 176px; line-height: 138px;
    letter-spacing: 2px;
    background: linear-gradient(90deg, var(--white) 0%, var(--ice) 45%, var(--sky) 100%);
    -webkit-background-clip: text; background-clip: text; color: transparent;
  }
  .tagline {
    position: absolute; left: 70px; top: 784px;
    font-weight: 800; font-size: 48px; line-height: 60px; color: var(--white);
    text-transform: uppercase;
  }
  .tagline em { font-style: normal; color: var(--accent); }
  .tagline-rule { position: absolute; left: 70px; top: 1074px; width: 326px; height: 5px; background: var(--white); }
  .tagline-close { top: 1124px; }

  .divider-band { position: absolute; left: 0; top: 1996px; }

  .intro {
    position: absolute; left: 70px; top: 2070px; width: 1060px;
    font-size: 37px; line-height: 52px; color: var(--ink); text-align: justify;
  }
  .intro strong { font-weight: 700; }

  .offer-col { position: absolute; top: 2396px; }
  .offer-col.solutions { left: 70px; }
  .offer-col.products { left: 636px; }
  .offer-title { font-weight: 800; font-size: 30px; line-height: 34px; color: var(--ink); text-transform: uppercase; height: 130px; }
  .offer-list { list-style: none; }
  .offer-list li {
    display: flex; align-items: center; gap: 38px; height: 59px;
    font-weight: 700; font-size: 31px; color: var(--ink);
  }
  .offer-list svg { flex: none; }
  .offer-rule { position: absolute; left: 580px; top: 2400px; width: 3px; height: 460px; background: var(--ink); }

  .corner-chevrons { position: absolute; right: 0; top: 2480px; }

  .footer {
    position: absolute; left: 0; top: 2922px; width: 1200px; height: 78px;
    background: var(--navy); color: var(--white);
    display: flex; align-items: center; justify-content: center;
    font-weight: 700; font-size: 30px;
  }
</style>
</head>
<body>
  <section class="hero">
    <div class="hero-photo" role="img" aria-label="Two American football players colliding in a stadium, one leaping with the ball"></div>

    <svg class="hero-stripes" width="520" height="270" viewBox="0 0 520 270" aria-hidden="true">
      <polygon points="0,0 46,0 316,270 270,270" fill="#2f7fd6"/>
      <polygon points="80,0 126,0 396,270 350,270" fill="#5fb4ee"/>
      <polygon points="160,0 206,0 476,270 430,270" fill="#1f5fc4"/>
      <polygon points="240,0 300,0 520,220 520,270 510,270" fill="#0b3a94"/>
    </svg>

    <svg class="hero-chevrons" width="250" height="540" viewBox="0 0 250 540" aria-hidden="true">
      <polygon points="0,0 40,0 250,270 40,540 0,540 0,500 180,270 0,40" fill="#5fb4ee"/>
      <polygon points="0,110 110,270 0,430" fill="#1f5fc4"/>
    </svg>

    <div class="brand"><span class="brand-square"></span>RVM</div>

    <h1 class="headline">Need Financing<br>For A Win?</h1>

    <p class="tagline">Winning teams<br><em>don’t</em> leave<br>success<br>to chance</p>
    <div class="tagline-rule"></div>
    <p class="tagline tagline-close">They build a<br>solid game plan.</p>
  </section>

  <svg class="divider-band" width="1200" height="60" viewBox="0 0 1200 60" aria-hidden="true">
    <rect x="0" y="0" width="1200" height="8" fill="#ffffff"/>
    <rect x="0" y="8" width="1200" height="46" fill="#0b3a94"/>
    <polygon points="290,8 390,8 360,54 260,54" fill="#ffffff"/>
    <polygon points="318,8 360,8 330,54 296,54" fill="#0c1d4f"/>
  </svg>

  <p class="intro">Whether you’re expanding, constructing, refinancing, or making key acquisitions, RVM provides financing solutions that help you execute your strategy with confidence. <strong>Let’s work together to create a winning playbook.</strong></p>

  <div class="offer-col solutions">
    <h2 class="offer-title">Our custom financing<br>solutions include:</h2>
    <ul class="offer-list">
      <li><svg width="32" height="32" viewBox="0 0 32 32" aria-hidden="true"><ellipse cx="16" cy="16" rx="15" ry="10" transform="rotate(-40 16 16)" fill="#7a3e1e"/><line x1="11" y1="21" x2="21" y2="11" stroke="#fff" stroke-width="2"/></svg>Acquisitions</li>
      <li><svg width="32" height="32" viewBox="0 0 32 32" aria-hidden="true"><ellipse cx="16" cy="16" rx="15" ry="10" transform="rotate(-40 16 16)" fill="#7a3e1e"/><line x1="11" y1="21" x2="21" y2="11" stroke="#fff" stroke-width="2"/></svg>Construction</li>
      <li><svg width="32" height="32" viewBox="0 0 32 32" aria-hidden="true"><ellipse cx="16" cy="16" rx="15" ry="10" transform="rotate(-40 16 16)" fill="#7a3e1e"/><line x1="11" y1="21" x2="21" y2="11" stroke="#fff" stroke-width="2"/></svg>Refinancing</li>
      <li><svg width="32" height="32" viewBox="0 0 32 32" aria-hidden="true"><ellipse cx="16" cy="16" rx="15" ry="10" transform="rotate(-40 16 16)" fill="#7a3e1e"/><line x1="11" y1="21" x2="21" y2="11" stroke="#fff" stroke-width="2"/></svg>Recapitalizations</li>
      <li><svg width="32" height="32" viewBox="0 0 32 32" aria-hidden="true"><ellipse cx="16" cy="16" rx="15" ry="10" transform="rotate(-40 16 16)" fill="#7a3e1e"/><line x1="11" y1="21" x2="21" y2="11" stroke="#fff" stroke-width="2"/></svg>Structured Leases</li>
    </ul>
  </div>

  <div class="offer-rule"></div>

  <div class="offer-col products">
    <h2 class="offer-title">Our products<br>include:</h2>
    <ul class="offer-list">
      <li><svg width="32" height="34" viewBox="0 0 32 34" aria-hidden="true"><path d="M6 2h20v8a10 10 0 0 1-20 0z" fill="#f0b323"/><rect x="13" y="19" width="6" height="7" fill="#d99a12"/><rect x="8" y="26" width="16" height="6" fill="#f0b323"/></svg>Bridge</li>
      <li><svg width="32" height="34" viewBox="0 0 32 34" aria-hidden="true"><path d="M6 2h20v8a10 10 0 0 1-20 0z" fill="#f0b323"/><rect x="13" y="19" width="6" height="7" fill="#d99a12"/><rect x="8" y="26" width="16" height="6" fill="#f0b323"/></svg>Mezzanine</li>
      <li><svg width="32" height="34" viewBox="0 0 32 34" aria-hidden="true"><path d="M6 2h20v8a10 10 0 0 1-20 0z" fill="#f0b323"/><rect x="13" y="19" width="6" height="7" fill="#d99a12"/><rect x="8" y="26" width="16" height="6" fill="#f0b323"/></svg>Unitranche</li>
      <li><svg width="32" height="34" viewBox="0 0 32 34" aria-hidden="true"><path d="M6 2h20v8a10 10 0 0 1-20 0z" fill="#f0b323"/><rect x="13" y="19" width="6" height="7" fill="#d99a12"/><rect x="8" y="26" width="16" height="6" fill="#f0b323"/></svg>NNN Lease</li>
      <li><svg width="32" height="34" viewBox="0 0 32 34" aria-hidden="true"><path d="M6 2h20v8a10 10 0 0 1-20 0z" fill="#f0b323"/><rect x="13" y="19" width="6" height="7" fill="#d99a12"/><rect x="8" y="26" width="16" height="6" fill="#f0b323"/></svg>Preferred Equity</li>
    </ul>
  </div>

  <svg class="corner-chevrons" width="180" height="300" viewBox="0 0 180 300" aria-hidden="true">
    <polygon points="180,0 180,36 58,150 180,264 180,300 18,150" fill="#c9e6fb"/>
    <polygon points="180,54 180,90 102,150 180,210 180,246 62,150" fill="#8fc8f2"/>
    <polygon points="180,108 180,192 134,150" fill="#5fb4ee"/>
  </svg>

  <footer class="footer">www.rvmcapital.com</footer>
</body>
</html>
```